Voltline Assemblies, Inc. Business Card

Voltline has three operating entities and I'm looking for a standard business card template that can be used for Voltline and the three operating entities that the logo just get swapped out, but has a very similar look and feel. Ultimately if someone had a business card from each, they assume the organizations are related because they all have the same look and feel.
Below are our websites and I will attached the logos for each entity:
https://www.voltlineassemblies.example/
https://www.brantoceramic.example/
https://www.omra-kfsd.example/
https://www.summitbreaker.example/

Target Market(s)

US Voltline

Industry/Entity Type

US Voltline

Contact Information for Business Card

Normal stuff

```html
<!DOCTYPE html>
<html lang="en">
<head>
<meta charset="utf-8">
<title>Voltline Assemblies, Inc. – Business Card Set</title>
<link rel="stylesheet" href="https://fonts.googleapis.com/css2?family=Encode+Sans+Condensed:wght@300;400;700;800&family=Fira+Sans:wght@600;700&display=swap">
<style>
  :root{
    --page:#cccccc;
    --navy:#001a87;
    --red:#c8102e;
    --ink:#1a1a1a;
    --white:#ffffff;
    --slate:#3e6a86;
  }
  *{box-sizing:border-box;margin:0;padding:0}
  html,body{width:848px;height:1200px;overflow:hidden;background:var(--page)}
  .sheet{position:relative;width:848px;height:1200px;font-family:"Encode Sans Condensed",sans-serif}
  .card{position:absolute;width:359px;height:205px;overflow:hidden}
  .card-front{left:55px;background:var(--white);border:0.6px solid #333}
  .card-back{left:434px;background:var(--navy)}
  .row-1{top:68px}.row-2{top:354px}.row-3{top:640px}.row-4{top:926px}

  .brand{position:absolute;display:flex;align-items:center;gap:6px;color:var(--navy)}
  .brand-dot{flex:none;border-radius:50%;background:var(--navy)}
  .brand-name{font-weight:800;line-height:1;white-space:nowrap}
  .brand-tag{position:absolute;font-family:"Fira Sans",sans-serif;font-weight:600;font-size:6.4px;color:var(--navy);white-space:nowrap}

  .person{position:absolute;font-size:8.6px;color:var(--ink);line-height:1}
  .person-name{color:var(--red);font-weight:700;font-size:11px;margin-bottom:6px}
  .person-role{font-weight:300;font-size:9.4px;margin-bottom:8px}
  .contact{display:flex;align-items:center;gap:3px;font-weight:300;font-size:9.4px;height:14.5px;margin-left:-15px}
  .contact svg{width:12px;height:12px;flex:none}
  .site{position:absolute;color:var(--red);font-weight:400;font-size:9.6px;letter-spacing:.1px}

  .footer-rule{position:absolute;left:0;right:0;top:178px;height:3px;background:var(--red)}
  .footer{position:absolute;left:0;right:0;top:181px;bottom:0;background:var(--navy);color:var(--white);
    font-family:"Fira Sans",sans-serif;font-weight:700;font-size:9.6px;letter-spacing:1.1px;
    display:flex;align-items:center;justify-content:center}

  .back-brand{position:absolute;left:43px;top:66px;display:flex;align-items:center;gap:12px;color:var(--white)}
  .back-brand .brand-dot{width:72px;height:72px;background:var(--white)}
  .back-brand .brand-name{font-size:27px;font-weight:800;line-height:1.05;white-space:normal;width:210px;text-transform:uppercase}
</style>
</head>
<body>
<svg width="0" height="0" style="position:absolute" aria-hidden="true">
  <defs>
    <symbol id="icon-phone" viewBox="0 0 24 24">
      <path d="M7 2c-2 1-3.5 3-3.5 6 0 6 4 12 9 14 2 .6 3.5-.3 4.2-1.6l-3.2-3.4-2 1c-2-1.4-3.4-4-3.6-6.5l1.8-1.3L8.7 2.4z" fill="#c8102e"/>
      <path d="M14 8a3 3 0 0 1 1.8 4M16.5 6a6 6 0 0 1 2 6.5" stroke="#c8102e" stroke-width="1.4" fill="none" stroke-linecap="round"/>
    </symbol>
    <symbol id="icon-mail" viewBox="0 0 24 24">
      <rect x="2" y="6" width="20" height="13" fill="#c8102e"/>
      <path d="M2 6l10 7 10-7M2 19l7-6M22 19l-7-6" stroke="#fff" stroke-width="1.2" fill="none"/>
    </symbol>
  </defs>
</svg>

<main class="sheet">

  <!-- Voltline -->
  <section class="card card-front row-1">
    <div class="brand" style="left:41px;top:26px">
      <span class="brand-dot" style="width:50px;height:50px"></span>
      <span class="brand-name" style="font-size:18px">VOLTLINE ASSEMBLIES, INC.</span>
    </div>
    <div class="person" style="left:40px;top:96px">
      <p class="person-name">Name Lastname</p>
      <p class="person-role">POSITION</p>
      <p class="contact"><svg><use href="#icon-phone"/></svg>123-456-7890</p>
      <p class="contact"><svg><use href="#icon-mail"/></svg>info@voltlineassemblies.example</p>
    </div>
    <a class="site" style="left:180px;top:144px">WWW.VOLTLINEASSEMBLIES.EXAMPLE</a>
    <div class="footer-rule"></div>
    <p class="footer">4180 Ridgeline Drive, Suite 210, Fairhaven, AL 35090</p>
  </section>
  <section class="card card-back row-1">
    <div class="back-brand"><span class="brand-dot"></span><span class="brand-name">Voltline Assemblies, Inc.</span></div>
  </section>

  <!-- Omra -->
  <section class="card card-front row-2">
    <div class="brand" style="left:65px;top:31px">
      <span class="brand-dot" style="width:32px;height:32px"></span>
      <span class="brand-name" style="font-size:17px">OMRA TRANSFORMER WORKS</span>
    </div>
    <p class="brand-tag" style="left:152px;top:67px">A Voltline Assemblies, Inc. Company</p>
    <div class="person" style="left:81px;top:96px">
      <p class="person-name">Name Lastname</p>
      <p class="person-role">POSITION</p>
      <p class="contact"><svg><use href="#icon-phone"/></svg>704-555-0148</p>
      <p class="contact"><svg><use href="#icon-mail"/></svg>sales@omra-kfsd.example</p>
    </div>
    <a class="site" style="left:197px;top:144px">WWW.OMRA-KFSD.EXAMPLE</a>
    <div class="footer-rule"></div>
    <p class="footer">1875 Millbrook Avenue, Dalton, NC 28190</p>
  </section>
  <section class="card card-back row-2">
    <div class="back-brand"><span class="brand-dot"></span><span class="brand-name">Voltline Assemblies, Inc.</span></div>
  </section>

  <!-- Branto -->
  <section class="card card-front row-3">
    <div class="brand" style="left:57px;top:31px">
      <span class="brand-dot" style="width:46px;height:46px"></span>
      <span class="brand-name" style="font-size:17px">BRANTO CERAMIC, LLC.</span>
    </div>
    <p class="brand-tag" style="left:123px;top:68px">A Voltline Assemblies, Inc. Company</p>
    <div class="person" style="left:57px;top:99px">
      <p class="person-name">Name Lastname</p>
      <p class="person-role">POSITION</p>
      <p class="contact"><svg><use href="#icon-phone"/></svg>304-555-0172</p>
      <p class="contact"><svg><use href="#icon-mail"/></svg>sales@brantoceramic.example</p>
    </div>
    <a class="site" style="left:180px;top:147px">WWW.BRANTOCERAMIC.EXAMPLE</a>
    <div class="footer-rule"></div>
    <p class="footer">612 W. County Rd 9, Suite 3, Harlow OH, 44490</p>
  </section>
  <section class="card card-back row-3">
    <div class="back-brand"><span class="brand-dot"></span><span class="brand-name">Voltline Assemblies, Inc.</span></div>
  </section>

  <!-- Summit -->
  <section class="card card-front row-4">
    <div class="brand" style="left:57px;top:26px;color:var(--slate)">
      <span class="brand-dot" style="width:50px;height:50px;background:var(--slate)"></span>
      <span class="brand-name" style="font-size:17px">SUMMIT BREAKER</span>
    </div>
    <p class="brand-tag" style="left:122px;top:69px">A Voltline Assemblies, Inc. Company</p>
    <div class="person" style="left:54px;top:99px">
      <p class="person-name">Name Lastname</p>
      <p class="person-role">POSITION</p>
      <p class="contact"><svg><use href="#icon-phone"/></svg>800-555-0136</p>
      <p class="contact"><svg><use href="#icon-mail"/></svg>sales@summitbreaker.example</p>
    </div>
    <a class="site" style="left:180px;top:147px">WWW.SUMMITBREAKER.EXAMPLE</a>
    <div class="footer-rule"></div>
    <p class="footer">2740 Cedar Lane SE, Fairhaven, AL 35090</p>
  </section>
  <section class="card card-back row-4">
    <div class="back-brand"><span class="brand-dot"></span><span class="brand-name">Voltline Assemblies, Inc.</span></div>
  </section>

</main>
</body>
</html>
```